B2B flyer solution for charging infrastructures (One-Pager Din A4, double-sided)

We need a professional design for our flyer in format Din A4/both sides.
Attached you will find the content for the flyer, but we are looking for a modern, professional design.

Some background/context information:
- the product is about a solution for charging and billing of charging infrastructures (for electric cars) in companies
- target group: companies, esp. facility managers, fleet managers, controlling, CTO, CEO
- should be printed and available online
- our website (and most of our current design work): https://wendo-kraft.de

In the files you will find:
- photos of reference implementations of our solution (should be included in the flyer)
- stock photos (we are using the one you will find in the current flyer on our presentations, maybe you can use it too to keep some corporate identity.
- our logo
- the current flyer as PDF and as PowerPoint
- a sample presentation we also need for customer communication

It would be nice if the design will align with the existing design work, but bring fresh aspects and will be up-to-date and professional.

Target Market(s)

B2B, companies, fleet managers, facility managers, CTO, CIO

Industry/Entity Type

Enterprises, Charging Solutions for Electric Vehicles

Requirements
Nice to have
• Bright, light design, clean, readable

```html
<!DOCTYPE html>
<html lang="de">
<head>
<meta charset="utf-8">
<title>wendo-kraft Professional – Flyer</title>
<link rel="stylesheet" href="https://fonts.googleapis.com/css2?family=Titillium+Web:ital,wght@0,300;0,400;0,600;0,700;1,300&display=swap">
<style>
:root{
  --bg:#c9c9c9;
  --paper:#ffffff;
  --navy:#1b2236;
  --pink:#e43f9b;
  --purple:#6a5cc0;
  --ink:#1f1f24;
  --text:#333338;
  --grad:linear-gradient(90deg,var(--pink),var(--purple));
}
*{box-sizing:border-box;margin:0;padding:0}
html,body{width:1200px;height:839px;overflow:hidden;background:var(--bg)}
body{position:relative;font-family:"Titillium Web",Arial,sans-serif;color:var(--text)}
.page{position:absolute;width:826px;height:1168px;background:var(--paper);transform:scale(.6);transform-origin:0 0;overflow:hidden}
.page--front{left:73px;top:68px}
.page--back{left:631px;top:70px}
.hero{position:absolute;left:0;top:0;width:826px;height:310px}
.hero--front{background:radial-gradient(circle at 75% 55%,#4a5d8c 0%,#2a3454 35%,var(--navy) 70%)}
.hero--back{background:radial-gradient(circle at 75% 45%,#cfe2f3 0%,#7f9fc7 35%,#33466e 70%,var(--navy) 100%)}
.brand{position:absolute;left:42px;top:92px;display:flex;align-items:center;gap:12px;color:#fff;font-size:38px;font-weight:600;letter-spacing:.5px}
.brand__dot{width:18px;height:18px;border-radius:50%;background:var(--pink)}
.hero-title{position:absolute;left:0;top:162px;width:620px;height:106px;padding:18px 0 0 44px;background:linear-gradient(90deg,rgba(255,255,255,.92) 60%,rgba(255,255,255,0))}
.hero-title h1{font-size:46px;font-weight:700;line-height:1;color:var(--ink)}
.hero-title p{font-size:23px;font-weight:600;color:var(--ink);line-height:1.2;margin-top:4px}
.band{position:absolute;left:0;top:310px;width:826px;height:48px;background:var(--grad);color:#fff;font-size:20px;display:flex;align-items:center;justify-content:center}
.title{position:absolute;left:44px;top:372px;font-size:46px;font-weight:700;color:var(--pink);line-height:1.1}
.subtitle{position:absolute;left:44px;top:428px;font-size:23px;font-weight:600;color:var(--ink)}
.lead{position:absolute;left:44px;top:476px;font-size:24px;font-weight:600;color:var(--ink);line-height:30px}
.lead em{display:block;font-weight:300;color:var(--pink);margin-top:4px}
.services{position:absolute;left:44px;top:610px;width:370px}
.services h2{font-size:24px;font-weight:700;color:var(--ink);margin-bottom:6px}
.bullets{list-style:none}
.bullets li{position:relative;padding-left:11px;font-size:16px;line-height:20px;margin-bottom:10px;color:var(--ink)}
.bullets li::before{content:"";position:absolute;left:0;top:8px;width:4px;height:4px;background:currentColor}
.photo{position:absolute}
.photo--chargers{left:435px;top:603px;width:347px;height:269px;border-radius:0 0 60px 0;background:linear-gradient(180deg,#8fa56a 0%,#5d7246 45%,#9c9e98 70%,#6e706c 100%)}
.photo--car{left:486px;top:850px;width:309px;height:223px;border-radius:40px 0 0 0;background:linear-gradient(160deg,#8a8c90 0%,#4b4d52 45%,#1e1f23 75%,#3b3c40 100%)}
.card{position:absolute;top:902px;height:183px;border-radius:30px;background:linear-gradient(135deg,var(--pink),var(--purple));color:#fff;padding:18px 20px;overflow:hidden}
.card h3{font-size:19px;font-weight:700;margin-bottom:6px}
.card--benefits{left:29px;width:375px;padding:16px 12px 12px 16px}
.card--benefits h3{font-size:17px;line-height:21px;letter-spacing:-.3px;white-space:nowrap;margin-bottom:5px}
.card--contact{left:421px;width:376px;padding:20px 24px}
.card--contact h3{font-size:20px;margin-bottom:14px}
.card p{font-size:16px;font-weight:300;line-height:20px}
.card .bullets li{color:#fff;font-weight:300;font-size:15.5px;line-height:19px;margin-bottom:5px}
.footer{position:absolute;left:28px;right:28px;top:1120px;display:flex;justify-content:space-between;align-items:center}
.contact{display:flex;align-items:center;gap:10px;font-size:20px;font-weight:700;color:var(--ink)}
.contact svg{width:22px;height:22px}
.groups{position:absolute;left:0;top:405px;width:826px}
.group{position:absolute;width:200px;text-align:center;font-size:19px;font-weight:700;color:var(--ink);line-height:25px}
.group svg{display:block;margin:0 auto 8px;height:36px}
.section{position:absolute;width:380px}
.section h3{font-size:20px;font-weight:700;color:var(--pink);line-height:25px;margin-bottom:12px}
.section p{font-size:16px;font-weight:300;line-height:20px;color:var(--ink);margin-bottom:10px}
.section .bullets li{font-weight:600;margin-bottom:5px}
.section .bullets li::before{background:var(--pink)}
</style>
</head>
<body>
<svg width="0" height="0" style="position:absolute">
  <defs>
    <linearGradient id="g" x1="0" x2="1"><stop offset="0" stop-color="#e43f9b"/><stop offset="1" stop-color="#6a5cc0"/></linearGradient>
  </defs>
</svg>

<!-- Front side -->
<section class="page page--front">
  <div class="hero hero--front" role="img" aria-label="Ladestecker einer E-Auto-Ladesäule vor unscharfen Lichtern"></div>
  <div class="brand"><span class="brand__dot"></span>wendo-kraft.de</div>
  <div class="band">wendo-kraft - Die Abrechnungslösung für Lade-Infrastruktur in Unternehmen.</div>

  <h1 class="title">wendo-kraft Professional</h1>
  <p class="subtitle">die maßgeschneiderte B2B-Abrechnungslösung für Elektromobilität</p>
  <p class="lead">Lade-Infrastruktur-Abrechnungslösungen für Unternehmen,<br>damit Lade-Infrastruktur Erträge statt Kosten produziert.
    <em>So wird Lade-Infrastruktur von einer Kostenstelle zu einem Profitcenter</em></p>

  <div class="services">
    <h2>Leistungen:</h2>
    <ul class="bullets">
      <li>Vielseitige Abrechnungsmöglichkeiten für Fuhr park, Mitarbeiter, Partnerunternehmen, Mieter, Kunden und andere.</li>
      <li>Full-Service-Betreuung (Monitoring, Abrechnung, Benutzerbetreuung)</li>
      <li>Integration in ihre Unternehmensabläufe</li>
      <li>Berücksichtigung von Eigentümer/Mieter Kon stellationen</li>
    </ul>
  </div>
  <div class="photo photo--chargers" role="img" aria-label="Reihe von Ladesäulen auf einem Parkplatz mit Bäumen"></div>

  <div class="card card--benefits">
    <h3>Mit wendo-kraft Professional profitieren:</h3>
    <ul class="bullets">
      <li>Effizienter Verwaltung von Lade-Infrastruktur</li>
      <li>Umfassende Full-Service-Betreuung</li>
      <li>Nahtloser Integration in Ihre kaufmännischen Prozesse</li>
      <li>Vielseitigen Abrechnungsmöglichkeiten</li>
    </ul>
  </div>
  <div class="card card--contact">
    <h3>Kontaktieren Sie uns</h3>
    <p>Erfahren Sie mehr über wendo-kraft und wie wir Ihre Abrechnungsanforderungen erfüllen können. Kontaktieren Sie uns für eine kosten+ lose Beratung:</p>
  </div>

  <div class="footer">
    <span class="contact"><svg viewBox="0 0 24 24" fill="none" stroke="url(#g)" stroke-width="2"><path d="M5 3h4l2 5-3 2a11 11 0 0 0 6 6l2-3 5 2v4a2 2 0 0 1-2 2A17 17 0 0 1 3 5a2 2 0 0 1 2-2z"/></svg>+49 (0) 9876 543 210</span>
    <span class="contact"><svg viewBox="0 0 24 24"><rect x="2" y="5" width="20" height="14" fill="url(#g)"/><path d="M2 5l10 8 10-8" fill="none" stroke="#fff" stroke-width="1.6"/></svg>info@wendo-kraft.de</span>
    <span class="contact"><svg viewBox="0 0 24 24" fill="none" stroke="url(#g)" stroke-width="1.6"><circle cx="12" cy="12" r="10"/><ellipse cx="12" cy="12" rx="4.5" ry="10"/><path d="M2 12h20M4 7h16M4 17h16"/></svg>www.wendo-kraft.de</span>
  </div>
</section>

<!-- Back side -->
<section class="page page--back">
  <div class="hero hero--back" role="img" aria-label="Elektroauto mit angeschlossenem Ladekabel und blau leuchtendem Ladeanschluss"></div>
  <div class="brand"><span class="brand__dot"></span>wendo-kraft.de</div>
  <div class="hero-title">
    <h1>wendo-kraft Professional</h1>
    <p>die Funktionen im Überblick</p>
  </div>
  <div class="band">wendo-kraft - Die Abrechnungslösung für Lade-Infrastruktur in Unternehmen.</div>

  <div class="groups">
    <div class="group" style="left:27px">
      <svg viewBox="0 0 72 30" width="72"><path d="M4 22v-7l8-2 8-7h26l10 7 10 2v7z" fill="none" stroke="url(#g)" stroke-width="3"/><circle cx="18" cy="23" r="4" fill="url(#g)"/><circle cx="52" cy="23" r="4" fill="url(#g)"/></svg>
      Fuhrpark,<br>Dienstwagen</div>
    <div class="group" style="left:223px">
      <svg viewBox="0 0 40 36" width="40"><circle cx="12" cy="9" r="6" fill="url(#g)"/><circle cx="28" cy="9" r="6" fill="url(#g)"/><circle cx="20" cy="17" r="6" fill="url(#g)"/><rect x="2" y="22" width="36" height="12" rx="6" fill="url(#g)"/></svg>
      Mitarbeiter<br>Privatfahrzeuge</div>
    <div class="group" style="left:415px">
      <svg viewBox="0 0 40 36" width="40"><circle cx="8" cy="12" r="5" fill="url(#g)"/><circle cx="32" cy="12" r="5" fill="url(#g)"/><circle cx="20" cy="7" r="6" fill="url(#g)"/><circle cx="20" cy="20" r="5" fill="url(#g)"/><rect x="2" y="24" width="36" height="11" rx="5" fill="url(#g)"/></svg>
      Kunden und<br>Gäste</div>
    <div class="group" style="left:605px">
      <svg viewBox="0 0 40 36" width="40"><rect x="4" y="14" width="10" height="22" fill="url(#g)"/><rect x="15" y="2" width="12" height="34" fill="url(#g)"/><rect x="28" y="20" width="9" height="16" fill="url(#g)"/></svg>
      Vermieter,<br>Eigentümer</div>
  </div>

  <div class="section" style="left:28px;top:533px">
    <h3>Full-Service-Betreuung<br>für sorgenfreies Management</h3>
    <p>wendo-kraft übernimmt auf Wunsch alle organisatorischen Belange bei der Verwaltung Ihrer Lade-Infrastruktur, einschließlich:</p>
    <ul class="bullets">
      <li>Monitoring</li>
      <li>Support</li>
      <li>User-Onboarding und -Support</li>
      <li>Handling von Zugangskarten</li>
      <li>Integration von firmeninternen Zugangstoken</li>
    </ul>
  </div>

  <div class="section" style="left:436px;top:533px;width:370px">
    <h3>Besonderer Aspekt: Eigentümer-<br>Mieter Konstellatione</h3>
    <p>Häufige Situation: Der Mieter eines Objektes benötigt Lade-Infrastruktur, der Eigentümer/ Verwalter möchte nicht zusätzlich belastet werden.</p>
    <ul class="bullets">
      <li>Unterschiedliche Betreibermodelle für verschiedene Situationen (Langzeit-Mieter vs. Kurzzeit-Mieter)</li>
      <li>Kauf-, Miet- und Leasing-Optionen</li>
      <li>Kostenneutral für Eigentümer/Verwalter durch geeingnete Abrechnungsmodelle</li>
    </ul>
  </div>

  <div class="section" style="left:28px;top:820px;width:440px">
    <h3>Perfekte Integration in<br>kaufmännische Prozesse</h3>
    <p>wendo-kraft fügt sich nahtlos in die kaufmännischen Strukturen moderner Unternehmen ein und bietet:</p>
    <ul class="bullets">
      <li>Erweitertes Reporting</li>
      <li>Aufschlüsselung und Tarifierung nach Nutzergruppe</li>
      <li>Unterstützung unternehmensinterner Abrechnung und Verrechnung und/oder Zahlungseinzug durch wendo-kraft</li>
      <li>Schnittstellen zu Buchhaltung und Lohnbuchhaltung</li>
      <li>Bedarfsgerechte Anpassbarkeit</li>
    </ul>
  </div>
  <div class="photo photo--car" role="img" aria-label="Dunkles Elektro-SUV an einer Wandladestation in einer Tiefgarage"></div>

  <div class="footer">
    <span class="contact"><svg viewBox="0 0 24 24" fill="none" stroke="url(#g)" stroke-width="2"><path d="M5 3h4l2 5-3 2a11 11 0 0 0 6 6l2-3 5 2v4a2 2 0 0 1-2 2A17 17 0 0 1 3 5a2 2 0 0 1 2-2z"/></svg>+49 (0) 9876 543 210</span>
    <span class="contact"><svg viewBox="0 0 24 24"><rect x="2" y="5" width="20" height="14" fill="url(#g)"/><path d="M2 5l10 8 10-8" fill="none" stroke="#fff" stroke-width="1.6"/></svg>info@wendo-kraft.de</span>
    <span class="contact"><svg viewBox="0 0 24 24" fill="none" stroke="url(#g)" stroke-width="1.6"><circle cx="12" cy="12" r="10"/><ellipse cx="12" cy="12" rx="4.5" ry="10"/><path d="M2 12h20M4 7h16M4 17h16"/></svg>www.wendo-kraft.de</span>
  </div>
</section>
</body>
</html>
```